curtainmaker, indoor and outdoor blind supplier

looking for logo to use for business cards and letter heads, I make all curtains for my clients and supply all kinds of blinds indoor and out. I'm looking for a design maybe with fabric background,

Industry/Entity Type

Business

Contact Information for Business Card

Moira Delaney Curtain Designs 14 Perriwick Drive Kellerton 3291. phone 03 55847391 mobile 0428936054, email moiradelaneycurtaindesign@tarvomail.com website moiradelaneycurtaindesigns.example.au/

Requirements
Nice to have
• maybe something in relation to sewing as an option

```html
<!DOCTYPE html>
<html lang="en">
<head>
<meta charset="utf-8">
<title>Moira Delaney Curtain Designs — Business Card</title>
<link href="https://fonts.googleapis.com/css2?family=Lato:wght@300;400;700&display=swap" rel="stylesheet">
<style>
  :root {
    --stage: #2b2b2d;
    --paper: #f1eff0;
    --paper-shade: #e4e1e3;
    --plum: #a8379b;
    --plum-light: #c155b3;
    --plum-deep: #7d2273;
    --rose: #e77fbf;
    --rose-soft: #f3b6d9;
    --white: #ffffff;
    --muted: #f0d3ea;
  }
  * { box-sizing: border-box; margin: 0; padding: 0; }
  html, body { width: 1200px; height: 1000px; overflow: hidden; }
  body {
    background: var(--stage);
    font-family: "Lato", Arial, sans-serif;
    display: flex;
    flex-direction: column;
    align-items: center;
    justify-content: center;
    gap: 70px;
  }
  .card {
    width: 640px;
    height: 360px;
    position: relative;
    background: linear-gradient(135deg, var(--paper), var(--paper-shade));
    box-shadow: 0 14px 30px rgba(0,0,0,.45);
    overflow: hidden;
  }
  .brand {
    display: flex;
    align-items: center;
    gap: 12px;
    color: var(--rose);
    font-weight: 400;
    line-height: 1.15;
  }
  .brand-dot {
    flex: none;
    border-radius: 50%;
    background: var(--plum);
  }
  /* front */
  .card-front .brand-area {
    position: absolute; left: 0; top: 0; width: 250px; height: 100%;
    display: flex; align-items: center; justify-content: center;
  }
  .card-front .brand { font-size: 21px; width: 200px; }
  .card-front .brand-dot { width: 26px; height: 26px; }
  .info-band {
    position: absolute; left: 250px; top: 0; width: 340px; height: 100%;
    background: linear-gradient(90deg, var(--plum-light), var(--plum));
    color: var(--white);
    padding: 40px 28px;
    display: flex; flex-direction: column; justify-content: space-between;
  }
  .info-band::after {
    content: ""; position: absolute; right: 10px; top: 0; bottom: 0;
    width: 1px; background: var(--muted);
  }
  .contact-list { list-style: none; display: flex; flex-direction: column; gap: 9px; }
  .contact-list li { display: flex; align-items: center; gap: 9px; font-size: 12px; font-weight: 300; white-space: nowrap; }
  .contact-icon {
    width: 18px; height: 18px; border-radius: 50%;
    background: var(--rose-soft); flex: none;
    display: flex; align-items: center; justify-content: center;
  }
  .person-name { font-size: 30px; font-weight: 400; letter-spacing: .3px; }
  .person-role { font-size: 14px; font-weight: 300; color: var(--muted); margin: 2px 0 12px; }
  .edge-strip {
    position: absolute; right: 0; top: 0; width: 50px; height: 100%;
    background: var(--paper);
  }
  /* back */
  .card-back .brand-area {
    position: absolute; left: 0; top: 0; width: 560px; height: 100%;
    display: flex; align-items: center; justify-content: center;
  }
  .card-back .brand { font-size: 32px; width: 330px; }
  .card-back .brand-dot { width: 38px; height: 38px; }
  .web-strip {
    position: absolute; right: 0; top: 0; width: 80px; height: 100%;
    background: linear-gradient(90deg, var(--plum-light), var(--plum-deep));
    display: flex; align-items: center; justify-content: center;
  }
  .web-strip span {
    writing-mode: vertical-rl;
    color: var(--muted);
    font-size: 12px; font-weight: 300; letter-spacing: .4px;
  }
</style>
</head>
<body>

  <section class="card card-front" aria-label="Business card front">
    <div class="brand-area">
      <div class="brand"><span class="brand-dot"></span><span>Moira Delaney Curtain Designs</span></div>
    </div>
    <div class="info-band">
      <ul class="contact-list">
        <li><span class="contact-icon"><svg width="10" height="10" viewBox="0 0 10 10"><path d="M5 0.5a3 3 0 0 1 3 3c0 2.2-3 6-3 6s-3-3.8-3-6a3 3 0 0 1 3-3z" fill="#a8379b"/></svg></span>14 Perriwick Drive Kellerton 3291</li>
        <li><span class="contact-icon"><svg width="10" height="10" viewBox="0 0 10 10"><rect x="1" y="2.5" width="8" height="5.5" fill="none" stroke="#a8379b" stroke-width="1.2"/><path d="M1 2.5l4 3 4-3" fill="none" stroke="#a8379b" stroke-width="1.2"/></svg></span>moiradelaneycurtaindesign@tarvomail.com</li>
        <li><span class="contact-icon"><svg width="10" height="10" viewBox="0 0 10 10"><circle cx="5" cy="5" r="3.8" fill="none" stroke="#a8379b" stroke-width="1.1"/><path d="M1.2 5h7.6M5 1.2c-2 2.5-2 5 0 7.6M5 1.2c2 2.5 2 5 0 7.6" fill="none" stroke="#a8379b" stroke-width=".9"/></svg></span>moiradelaneycurtaindesigns.example.au/</li>
      </ul>
      <div class="person">
        <h1 class="person-name">Moira Delaney</h1>
        <p class="person-role">Owner/Chief Designer</p>
        <ul class="contact-list">
          <li><span class="contact-icon"><svg width="10" height="10" viewBox="0 0 10 10"><path d="M2.2 1l1.6 1.8-.9 1.3c.6 1.2 1.6 2.2 2.8 2.8l1.3-.9L9 7.8 7.8 9C4.3 8.6 1.4 5.7 1 2.2z" fill="#a8379b"/></svg></span>+03 55847391</li>
          <li><span class="contact-icon"><svg width="10" height="10" viewBox="0 0 10 10"><rect x="3" y="1" width="4" height="8" rx=".8" fill="none" stroke="#a8379b" stroke-width="1.1"/></svg></span>+0428936054</li>
        </ul>
      </div>
    </div>
    <div class="edge-strip"></div>
  </section>

  <section class="card card-back" aria-label="Business card back">
    <div class="brand-area">
      <div class="brand"><span class="brand-dot"></span><span>Moira Delaney Curtain Designs</span></div>
    </div>
    <div class="web-strip"><span>moiradelaneycurtaindesigns.example.au</span></div>
  </section>

</body>
</html>
```